Casa Morellina Togo Menu seperated in categories

new to go menu for italian restaurant with menu descriptions and prices i like the cover first page to have all the restaurant information, the other pages should be separated in the menu categories, and if we can include a map with the location of the restaurant
Casa Morellina
42 Route 58 S
North Myrtle Beach, SC 29582
open 7 days a week 4-10
Happy hour served Daily at the Bar 4-7
www.casamorellina.com
casamorellinadk@brivomail.com

Sans Serif

• Prices and pictures and restaurant information

```html
<!DOCTYPE html>
<html lang="en">
<head>
<meta charset="utf-8">
<title>Casa Morellina — To Go Menu, À la Carte</title>
<link rel="stylesheet" href="https://fonts.googleapis.com/css2?family=Didact+Gothic&family=Montserrat:wght@700&display=swap">
<style>
  :root {
    --backdrop: #cb8b5c;
    --panel: #f3f4f6;
    --basil: #3d8878;
    --cream: #ffffff;
    --tomato: #be1048;
    --ink: #1d1d1d;
    --crest: #f6df9a;
  }
  html, body {
    margin: 0;
    padding: 0;
    width: 849px;
    height: 1200px;
    overflow: hidden;
    background: var(--backdrop);
  }
  .menu-page {
    position: relative;
    width: 849px;
    height: 1200px;
    background: var(--backdrop);
    font-family: "Didact Gothic", "Century Gothic", sans-serif;
    color: var(--ink);
  }
  .scallop-frame {
    position: absolute;
    inset: 0;
  }
  .brand-watermark {
    position: absolute;
    left: 107px;
    top: 420px;
    width: 635px;
    margin: 0;
    text-align: center;
    font-family: "Didact Gothic", "Century Gothic", sans-serif;
    font-weight: 400;
    font-size: 104px;
    line-height: 118px;
    color: var(--crest);
    letter-spacing: 1px;
  }
  .menu-content {
    position: absolute;
    left: 107px;
    top: 98px;
    width: 635px;
    text-align: center;
  }
  .section-title {
    margin: 18px 0 0;
    font-family: "Montserrat", sans-serif;
    font-weight: 700;
    font-size: 20px;
    line-height: 24px;
    color: var(--basil);
    letter-spacing: 0.3px;
  }
  .section-note {
    margin: 0;
    font-size: 19px;
    line-height: 22px;
  }
  .item-list {
    list-style: none;
    margin: 18px 0 0;
    padding: 0;
    font-size: 19px;
    line-height: 21px;
  }
  .menu-notice {
    margin: 60px 0 0;
    font-family: "Montserrat", sans-serif;
    font-weight: 700;
    font-size: 19.8px;
    line-height: 28px;
    color: var(--basil);
    letter-spacing: 0.2px;
  }
</style>
</head>
<body>
<div class="menu-page">
  <svg class="scallop-frame" width="849" height="1200" viewBox="0 0 849 1200">
    <defs>
      <pattern id="tabs-top" patternUnits="userSpaceOnUse" x="107" y="48" width="105.9" height="60">
        <rect x="0" y="0" width="35.3" height="60" rx="17.6" fill="var(--basil)"/>
        <rect x="35.3" y="0" width="35.3" height="60" rx="17.6" fill="var(--cream)"/>
        <rect x="70.6" y="0" width="35.3" height="60" rx="17.6" fill="var(--tomato)"/>
      </pattern>
      <pattern id="tabs-side-left" patternUnits="userSpaceOnUse" x="57" y="98" width="60" height="107.1">
        <rect x="0" y="0" width="60" height="35.7" rx="17.8" fill="var(--tomato)"/>
        <rect x="0" y="35.7" width="60" height="35.7" rx="17.8" fill="var(--cream)"/>
        <rect x="0" y="71.4" width="60" height="35.7" rx="17.8" fill="var(--basil)"/>
      </pattern>
      <pattern id="tabs-side-right" patternUnits="userSpaceOnUse" x="732" y="98" width="60" height="107.1">
        <rect x="0" y="0" width="60" height="35.7" rx="17.8" fill="var(--basil)"/>
        <rect x="0" y="35.7" width="60" height="35.7" rx="17.8" fill="var(--cream)"/>
        <rect x="0" y="71.4" width="60" height="35.7" rx="17.8" fill="var(--tomato)"/>
      </pattern>
      <pattern id="tabs-bottom" patternUnits="userSpaceOnUse" x="107" y="1090" width="105.9" height="60">
        <rect x="0" y="0" width="35.3" height="60" rx="17.6" fill="var(--basil)"/>
        <rect x="35.3" y="0" width="35.3" height="60" rx="17.6" fill="var(--cream)"/>
        <rect x="70.6" y="0" width="35.3" height="60" rx="17.6" fill="var(--tomato)"/>
      </pattern>
      <linearGradient id="room-tones" x1="0.15" y1="0.1" x2="0.85" y2="0.95">
        <stop offset="0" stop-color="#c9582e"/>
        <stop offset="0.28" stop-color="#e8622c"/>
        <stop offset="0.5" stop-color="#b8662e"/>
        <stop offset="0.68" stop-color="#7a4424"/>
        <stop offset="0.85" stop-color="#2e1a14"/>
        <stop offset="1" stop-color="#15100e"/>
      </linearGradient>
    </defs>
    <rect x="107" y="48" width="635" height="60" fill="url(#tabs-top)"/>
    <rect x="107" y="1090" width="635" height="60" fill="url(#tabs-bottom)"/>
    <rect x="57" y="98" width="60" height="1000" fill="url(#tabs-side-left)"/>
    <rect x="732" y="98" width="60" height="1000" fill="url(#tabs-side-right)"/>
    <rect class="menu-panel" x="107" y="98" width="635" height="1002" fill="var(--panel)"/>
    <ellipse class="accent-crescent" cx="421" cy="866" rx="265" ry="170" fill="var(--basil)"/>
    <ellipse class="dining-room" cx="446" cy="871" rx="234" ry="163" fill="url(#room-tones)" role="img" aria-label="Photo of the restaurant's piano lounge with stone walls, a glowing red chalkboard wall, a black grand piano and wine shelves"/>
  </svg>

  <p class="brand-watermark">Casa<br>Morellina</p>

  <main class="menu-content">
    <h1 class="section-title">ALA CARTE</h1>
    <p class="section-note">Not Available as an Entrée, Add on Only</p>
    <ul class="item-list">
      <li>Meatballs 4.95</li>
      <li>Sausage 4.95</li>
      <li>Veggie of the Day 4.95</li>
      <li>Fettuccine Alfredo 4.95</li>
      <li>Spaghetti Bolognese 4.95</li>
    </ul>
    <p class="menu-notice">ALL OF MENU IS SUBJECT TO CHANGE<br>DAILY SPECIALS AVAILABLE</p>
  </main>
</div>
</body>
</html>
```